Website for a web design agency

We are a website and marketing agency. We do website design, development, and well as Brindle and Quorvia advertising and analytics. We ourselves need a new website for our own brand. We are working on some designs in-house with our own designers, but we also wanted to see what outside designers would come up with.
We are starting off with the homepage, and here is the breakdown of the sections:
https://files.brindlework.example/sheet/d/7kqTr2VnPLwXeHsaMcY4oBfJzuGNtKdWiEh3Rx9pLmQb/view?mode=share
This doc also has many links to sites we have done, which you can take screenshots of for the portfolio section.
In terms of the "look" I am going for, I want to look high-end and very beautiful designs. I found this website that I like a lot that you can use some of the elements of, just as a starting point:
http://velmarkstudio.example/layouts/pixelbarn/html/ostrevo/index.html and here is another design option they have http://velmarkstudio.example/layouts/pixelbarn/html/ostrevo/index-4.html
I'm also uploading my logo. The logo matches the gold and black look from these websites, but I would be open to switching to another color scheme if needed.
This is the link to my very old website, which you can use for some of the dummy text, and a pic of myself. I will be taking more pics of myself:
https://theplumtreeandwillowgroup.example/
We need a homepage and a portfolio page right now, but if you are the winner, we will be hiring you to make additional pages.
Updates
More designs continue to come in even today, and I want to make sure no other designers are still submitting designs.
Target Market(s)
medium and large businesses owners, and non-profits
Number of Pages Required
1 page

```html
<!DOCTYPE html>
<html lang="en">
<head>
<meta charset="utf-8">
<title>Halvern Strategies — Home</title>
<link href="https://fonts.googleapis.com/css2?family=Nunito+Sans:wght@400;600;700;800;900&display=swap" rel="stylesheet">
<style>
:root{
  --gold:#f0b323;
  --gold-dark:#c18b12;
  --ink:#1d1d1d;
  --hero:#2a2a2a;
  --charcoal:#272727;
  --black:#050505;
  --slate:#232323;
  --footer:#1b1b1b;
  --white:#ffffff;
  --muted:#5a5a5a;
  --line:#d6d6d6;
}
*{box-sizing:border-box;margin:0;padding:0}
html,body{width:1200px;height:5222px;overflow:hidden}
body{font-family:"Nunito Sans",Arial,sans-serif;color:var(--white);background:var(--black);position:relative}
.section{position:absolute;left:0;width:1200px;overflow:hidden}
.abs{position:absolute}
.heading{position:absolute;left:0;width:1200px;text-align:center;font-weight:800;font-size:38px;color:var(--gold);letter-spacing:.5px}
.underline{position:absolute;left:552px;width:96px;height:4px;background:var(--gold)}

/* hero */
.hero{top:0;height:675px;background:linear-gradient(160deg,#343434 0%,var(--hero) 45%,#222 100%)}
.brand{position:absolute;left:172px;top:45px;width:193px;height:60px;border:1px solid #444;background:#1f1f1f;display:flex;flex-direction:column;justify-content:center;align-items:center}
.brand-name{font-weight:800;color:var(--gold);font-size:26px;letter-spacing:3px;line-height:1}
.brand-sub{font-weight:800;color:var(--gold);font-size:12px;letter-spacing:6px;line-height:1;margin-top:4px}
.nav{position:absolute;left:474px;top:66px;display:flex;gap:12px;font-size:14px;font-weight:600}
.btn{position:absolute;background:var(--gold);color:var(--white);border-radius:26px;font-weight:700;display:flex;align-items:center;justify-content:center}
.hero-title{left:172px;top:268px;font-size:42px;font-weight:800;letter-spacing:.5px}
.hero-sub{left:172px;top:344px;font-size:19px;line-height:33px;font-weight:600}
.video{left:567px;top:227px;width:523px;height:324px;background:linear-gradient(135deg,#8b8b8b,#5d5d5d 60%,#3e3e3e);border-top:10px solid #fff}
.video-name{position:absolute;left:12px;top:206px;font-size:30px;font-weight:700;color:#fff;letter-spacing:1px}
.video-bar{position:absolute;left:0;bottom:0;width:100%;height:28px;background:#111}

/* services */
.services{top:675px;height:720px;background:var(--charcoal)}
.card{position:absolute;top:282px;width:229px;height:251px;background:var(--gold);color:var(--ink);text-align:center;padding:0 14px}
.card.light{background:var(--white)}
.card-icon{position:absolute;left:70px;top:-41px;width:89px;height:89px;background:var(--white);border-radius:6px;box-shadow:0 3px 10px rgba(0,0,0,.25);display:flex;align-items:center;justify-content:center}
.card.light .card-icon{background:var(--gold)}
.card-title{margin-top:85px;font-size:18px;font-weight:600;letter-spacing:.3px}
.card-text{margin-top:10px;font-size:12px;line-height:20px}
.tail{position:absolute;top:251px;right:0}

/* portfolio */
.portfolio{top:1395px;height:723px;background:var(--black)}
.work{position:absolute;top:202px;width:352px;height:373px;background:var(--gold);color:var(--ink);text-align:center}
.shot{width:100%;height:244px}
.work-title{margin-top:16px;font-size:20px;font-weight:700}
.work-text{margin:8px 14px 0;font-size:12px;line-height:20px}
.dots{position:absolute;top:632px;left:566px;display:flex;gap:8px}
.dots span{width:16px;height:16px;border-radius:50%;background:#5a4a1c}
.dots span:first-child{background:var(--gold)}

/* testimonials */
.testimonials{top:2118px;height:720px;background:var(--slate)}
.quote{position:absolute;background:var(--gold);color:var(--ink);text-align:center;border-radius:8px}
.quote.main{background:var(--white);z-index:2;box-shadow:0 6px 24px rgba(0,0,0,.35)}
.quote-mark{position:absolute;left:50%;transform:translateX(-50%);background:var(--white);border-radius:6px;box-shadow:0 3px 8px rgba(0,0,0,.25);display:flex;align-items:center;justify-content:center}
.quote.main .quote-mark{background:var(--gold)}
.quote h3{font-weight:600;letter-spacing:.5px}
.quote p{line-height:1.6}
.quote a{color:var(--ink);text-decoration:underline}

/* team */
.team{top:2838px;height:551px;background:var(--slate)}
.team-title{left:172px;top:152px;font-size:38px;font-weight:800;color:var(--gold)}
.team-rule{left:172px;top:205px;width:96px;height:4px;background:var(--gold)}
.team-copy{left:172px;top:234px;width:302px;font-size:12px;line-height:27px;text-align:justify}
.member{position:absolute;top:97px;width:274px;height:339px;background:var(--white);color:var(--ink);text-align:center;padding:12px}
.member.gold{background:var(--gold)}
.member .photo{width:250px;height:186px}
.member h4{margin-top:28px;font-size:18px;font-weight:800}
.member .role{font-size:13px;color:var(--muted);margin-top:2px}
.member.gold .role{color:var(--ink)}
.member p{margin-top:14px;font-size:12px;line-height:20px;color:var(--muted)}
.member.gold p{color:var(--ink)}

/* benefits + audit */
.benefits{top:3389px;height:1178px;background:var(--charcoal)}
.lead{left:0;width:1200px;top:160px;text-align:center;font-size:15px;font-weight:700}
.perk{position:absolute;width:250px}
.perk-icon{width:40px;height:40px;border-radius:50%;background:var(--gold);display:flex;align-items:center;justify-content:center}
.perk h5{margin-top:12px;font-size:13px;font-weight:800;letter-spacing:.4px}
.perk p{margin-top:10px;font-size:12px;line-height:19px}
.portrait{left:726px;top:189px;width:308px;height:365px;background:linear-gradient(180deg,#3a3a3a 0%,#d9c3b0 55%,#efe4da 100%)}
.audit-title{top:608px}
.audit-block{left:0;top:888px;width:304px;height:290px;background:var(--gold)}
.audit-photo{left:172px;top:746px;width:396px;height:385px;background:linear-gradient(135deg,#f3f3f3,#cfc6bb 60%,#9b8c7d)}
.field{position:absolute;border:1px solid #cfcfcf;color:#e6e6e6;font-size:14px;padding:13px 10px}
.submit{position:absolute;left:604px;top:1034px;width:118px;height:49px;background:var(--gold);color:var(--ink);font-size:14px;font-weight:600;display:flex;align-items:center;justify-content:center}

/* footer */
.footer{top:4567px;height:655px;background:var(--footer)}
.footer-brand{left:440px;top:146px;width:322px;text-align:center;color:var(--gold);font-weight:800}
.contact{position:absolute;top:316px;width:260px;text-align:center}
.ring{width:74px;height:74px;margin:0 auto;border:2px solid var(--gold);border-radius:50%;display:flex;align-items:center;justify-content:center}
.contact .label{margin-top:32px;font-size:15px;color:var(--gold)}
.contact .value{margin-top:6px;font-size:21px;font-weight:800;color:var(--gold);line-height:32px}
.footer-rule{left:172px;top:557px;width:856px;height:1px;background:var(--gold)}
.copyright{left:0;width:1200px;top:600px;text-align:center;font-size:13px;color:var(--gold)}
.build{left:1092px;top:600px;font-size:13px;color:var(--gold)}
</style>
</head>
<body>

<header class="section hero">
  <div class="brand"><span class="brand-name">HALVERN</span><span class="brand-sub">STRATEGIES</span></div>
  <nav class="nav"><span>HOME</span><span>WHAT WE DO</span><span>PORTFOLIO</span><span>TEAM</span><span>CONTACT</span></nav>
  <div class="btn" style="left:857px;top:50px;width:160px;height:51px;font-size:13px">CONSULT WITH US</div>
  <h1 class="abs hero-title">WE BUILD VALUE</h1>
  <p class="abs hero-sub">Enterprise Level Website Development<br>and Online Marketing</p>
  <div class="btn" style="left:172px;top:442px;width:162px;height:50px;font-size:13px">SEE HOW WE DO IT</div>
  <div class="abs video" role="img" aria-label="Intro video still of the founder speaking to camera">
    <span class="video-name">Marcus Halvern</span>
    <div class="video-bar">
      <svg width="523" height="28"><polygon points="14,8 14,20 24,14" fill="#fff"/><rect x="40" y="13" width="440" height="3" fill="#555"/><rect x="40" y="13" width="18" height="3" fill="#ccc"/></svg>
    </div>
  </div>
</header>

<section class="section services">
  <h2 class="heading" style="top:74px">WHAT WE DO</h2>
  <div class="underline" style="top:130px"></div>

  <div class="card" style="left:120px">
    <div class="card-icon"><svg width="52" height="52" viewBox="0 0 52 52" fill="none" stroke="#222" stroke-width="2.5"><rect x="10" y="6" width="28" height="36" rx="2"/><path d="M16 16h16M16 23h16M16 30h10"/><path d="M34 34l10 10"/></svg></div>
    <h3 class="card-title">WEBSITES</h3>
    <p class="card-text">Whether you are just starting out or already a successful business, having a successful online presence is always a central part of your business.</p>
    <svg class="tail" width="110" height="50"><polygon points="0,0 110,0 0,50" fill="var(--gold-dark)"/></svg>
  </div>
  <div class="card light" style="left:363px">
    <div class="card-icon"><svg width="52" height="52" viewBox="0 0 52 52" fill="none" stroke="#222" stroke-width="2.5"><rect x="6" y="8" width="40" height="34" rx="3"/><path d="M6 16h40"/><circle cx="26" cy="29" r="9"/><path d="M17 29h18M26 20c-4 5-4 13 0 18M26 20c4 5 4 13 0 18"/></svg></div>
    <h3 class="card-title">LANDING PAGES</h3>
    <p class="card-text">Whether you are just starting out or already a successful business, having a successful online presence is always a central part of your business.</p>
    <svg class="tail" width="110" height="50"><polygon points="0,0 110,0 0,50" fill="#d7d7d7"/></svg>
  </div>
  <div class="card" style="left:608px">
    <div class="card-icon"><svg width="52" height="52" viewBox="0 0 52 52" fill="none" stroke="#222" stroke-width="2.5"><circle cx="30" cy="18" r="11"/><path d="M30 11v14M34 14c-2-2-8-2-8 1s8 2 8 5-6 3-8 1"/><path d="M6 36l8-4h10l10 4-10 8H12"/></svg></div>
    <h3 class="card-title">DONATION PAGES</h3>
    <p class="card-text">Whether you are just starting out or already a successful business, having a successful online presence is always a central part of your business.</p>
    <svg class="tail" width="110" height="50"><polygon points="0,0 110,0 0,50" fill="var(--gold-dark)"/></svg>
  </div>
  <div class="card" style="left:853px">
    <div class="card-icon"><svg width="52" height="52" viewBox="0 0 52 52" fill="none" stroke="#222" stroke-width="2.5"><rect x="6" y="8" width="40" height="34" rx="3"/><path d="M6 16h40"/><path d="M24 24l4 14 3-5 6 6 3-3-6-6 5-3z"/></svg></div>
    <h3 class="card-title">PPC AND FUNNELS</h3>
    <p class="card-text">Whether you are just starting out or already a successful business, having a successful online presence is always a central part of your business.</p>
    <svg class="tail" width="110" height="50"><polygon points="0,0 110,0 0,50" fill="var(--gold-dark)"/></svg>
  </div>
</section>

<section class="section portfolio">
  <h2 class="heading" style="top:74px">PORTFOLIO</h2>
  <div class="underline" style="top:130px"></div>

  <article class="work" style="left:36px">
    <div class="shot" role="img" aria-label="Homepage screenshot of the Orveto Productions site, deep blue underwater hero" style="background:linear-gradient(180deg,#fff 0 12%,#1a3d6d 12% 76%,#fff 76%)"></div>
    <h3 class="work-title">ORVETO PRODUCTIONS</h3>
    <p class="work-text">I want to build your site or get you higher on Brindle. Unlike big agencies, I want to hold your hand throughout the process.</p>
  </article>
  <article class="work" style="left:424px">
    <div class="shot" role="img" aria-label="Homepage screenshot of the Tamsinhal charity site, light blue hero with children" style="background:linear-gradient(180deg,#fff 0 9%,#8fc2e4 9% 82%,#f2f2f2 82%)"></div>
    <h3 class="work-title">TAMSINHAL</h3>
    <p class="work-text">I want to build your site or get you higher on Brindle. Unlike big agencies, I want to hold your hand throughout the process.</p>
  </article>
  <article class="work" style="left:811px">
    <div class="shot" role="img" aria-label="Homepage screenshot of the Nuvelline site, grey fitness hero" style="background:linear-gradient(180deg,#fff 0 7%,#9a9a9a 7% 88%,#fff 88%)"></div>
    <h3 class="work-title">NUVELLINE</h3>
    <p class="work-text">I want to build your site or get you higher on Brindle. Unlike big agencies, I want to hold your hand throughout the process.</p>
  </article>
  <div class="dots"><span></span><span></span><span></span></div>
</section>

<section class="section testimonials">
  <h2 class="heading" style="top:82px">TESTIMONIALS</h2>
  <div class="underline" style="top:138px"></div>

  <div class="quote" style="left:107px;top:300px;width:298px;height:217px">
    <div class="quote-mark" style="top:-36px;width:76px;height:76px"><svg width="40" height="32"><polygon points="8,0 18,0 10,32 0,32" fill="#222"/><polygon points="28,0 38,0 30,32 20,32" fill="#222"/></svg></div>
    <h3 style="margin-top:66px;font-size:16px">GOOD WORK</h3>
    <p style="margin:12px 10px 0;font-size:10px">Duis aute irure dolor in reprehenderit in voluptate velit esse cillum dolore eu fugiat nulla pariatur. Excepteur sint occaecat cupidatat non proident.</p>
    <p style="font-size:10px;margin-top:2px">- ELIAS BROOK</p>
    <p style="font-size:10px;margin-top:4px"><a>Lorem ipsum dolor sit amet, consectetur</a></p>
    <svg class="abs" style="left:230px;top:217px" width="68" height="40"><polygon points="0,0 68,0 0,40" fill="var(--gold-dark)"/></svg>
  </div>
  <div class="quote main" style="left:395px;top:268px;width:410px;height:280px">
    <div class="quote-mark" style="top:-46px;width:92px;height:92px"><svg width="48" height="40"><polygon points="10,0 22,0 12,40 0,40" fill="#222"/><polygon points="36,0 48,0 38,40 26,40" fill="#222"/></svg></div>
    <h3 style="margin-top:74px;font-size:21px">GOOD WORK</h3>
    <p style="margin:14px 18px 0;font-size:13px">Duis aute irure dolor in reprehenderit in voluptate velit esse cillum dolore eu fugiat nulla pariatur. Excepteur sint occaecat cupidatat non proident.</p>
    <p style="font-size:13px;margin-top:8px">- FARROW</p>
    <p style="font-size:11px;margin-top:4px"><a>Lorem ipsum dolor sit amet, consectetur</a></p>
    <svg class="abs" style="left:295px;top:280px" width="115" height="55"><polygon points="0,0 115,0 0,55" fill="#d7d7d7"/></svg>
  </div>
  <div class="quote" style="left:795px;top:300px;width:300px;height:217px">
    <div class="quote-mark" style="top:-36px;width:76px;height:76px;margin-left:5px"><svg width="40" height="32"><polygon points="8,0 18,0 10,32 0,32" fill="#222"/><polygon points="28,0 38,0 30,32 20,32" fill="#222"/></svg></div>
    <h3 style="margin-top:66px;font-size:16px;padding-left:10px">GOOD WORK</h3>
    <p style="margin:12px 10px 0 20px;font-size:10px">Duis aute irure dolor in reprehenderit in voluptate velit esse cillum dolore eu fugiat nulla pariatur. Excepteur sint occaecat cupidatat non proident.</p>
    <p style="font-size:10px;margin-top:2px;padding-left:10px">- LINNEA</p>
    <p style="font-size:10px;margin-top:4px;padding-left:10px"><a>Lorem ipsum dolor sit amet, consectetur</a></p>
    <svg class="abs" style="left:232px;top:217px" width="68" height="40"><polygon points="0,0 68,0 0,40" fill="var(--gold-dark)"/></svg>
  </div>
</section>

<section class="section team">
  <h2 class="abs team-title">OUR TEAM</h2>
  <div class="abs team-rule"></div>
  <p class="abs team-copy">Nemo enim ipsam voluptatem quia voluptas sit aspernatur aut odit aut fugit, sed quia consequuntur magni dolores eos qui ratione voluptatem sequi nesciunt. Neque porro quisquam est, qui dolorem ipsum quia dolor sit amet, consectetur, adipisci velit, sed quia non numquam.</p>

  <div class="member" style="left:515px">
    <div class="photo" role="img" aria-label="Portrait of team member Dorian Pell" style="background:linear-gradient(180deg,#c9ced3,#8a7a5c 70%,#b88a3c)"></div>
    <h4>DORIAN PELL</h4>
    <div class="role">CEO</div>
    <p>Sed ut perspiciatis unde omnis iste natus error sit voluptatem accusantium</p>
  </div>
  <div class="member gold" style="left:815px">
    <div class="photo" role="img" aria-label="Portrait of team member Cyrus Wendt" style="background:linear-gradient(180deg,#dfe3e6,#b4a08a 65%,#8d8d8d)"></div>
    <h4>CYRUS WENDT</h4>
    <div class="role">CEO</div>
    <p>Sed ut perspiciatis unde omnis iste natus error sit voluptatem accusantium</p>
  </div>
</section>

<section class="section benefits">
  <h2 class="heading" style="top:74px">WHAT YOU'LL GET</h2>
  <p class="abs lead">I want to share my values with you so you can see what it's like working with me.</p>

  <div class="perk" style="left:177px;top:219px">
    <div class="perk-icon"><svg width="20" height="20" viewBox="0 0 20 20"><path d="M3 10L10 3h7v7l-7 7z" fill="#fff"/><circle cx="14" cy="6" r="1.6" fill="var(--gold)"/></svg></div>
    <h5>AFFORDABLE PRICING</h5>
    <p>No small lettering or big corporations here. I promise to give you the best</p>
  </div>
  <div class="perk" style="left:458px;top:219px">
    <div class="perk-icon"><svg width="20" height="20" viewBox="0 0 20 20"><rect x="9" y="3" width="8" height="14" fill="#fff"/><path d="M2 10h9M8 7l3 3-3 3" stroke="#fff" stroke-width="2" fill="none"/></svg></div>
    <h5>ACCESSIBILITY</h5>
    <p>You get my actual cell phone number and are welcome to call me 24/7</p>
  </div>
  <div class="perk" style="left:177px;top:376px">
    <div class="perk-icon"><svg width="22" height="20" viewBox="0 0 22 20"><path d="M2 6l5 4 4-7 4 7 5-4-2 10H4z" fill="#fff"/></svg></div>
    <h5>CREATIVITY</h5>
    <p>Struggling with what exactly you need? No problem! I'm here to be</p>
  </div>
  <div class="perk" style="left:458px;top:376px">
    <div class="perk-icon"><svg width="20" height="20" viewBox="0 0 20 20"><path d="M10 17L3 10a4 4 0 016-5l1 1 1-1a4 4 0 016 5z" fill="#fff"/></svg></div>
    <h5>DOWNRIGHT LOVE</h5>
    <p>Yes, I put my sweat tears and energy into my projects and my customers.</p>
  </div>
  <div class="abs portrait" role="img" aria-label="Portrait of the founder in a light shirt"></div>

  <h2 class="heading audit-title">GET A FREE AUDIT AND CONSULTATION</h2>
  <div class="underline" style="top:663px"></div>
  <div class="abs audit-block"></div>
  <div class="abs audit-photo" role="img" aria-label="Support team members wearing headsets at their desks"></div>
  <div class="field" style="left:604px;top:777px;width:207px;height:50px">First Name</div>
  <div class="field" style="left:821px;top:777px;width:205px;height:50px">Last Name</div>
  <div class="field" style="left:604px;top:843px;width:207px;height:51px">Email</div>
  <div class="field" style="left:821px;top:843px;width:205px;height:51px">Phone</div>
  <div class="field" style="left:604px;top:912px;width:422px;height:98px">Message</div>
  <div class="submit">SUBMIT</div>
</section>

<footer class="section footer">
  <div class="abs footer-brand"><div style="font-size:60px;letter-spacing:6px;line-height:1">HALVERN</div><div style="font-size:25px;letter-spacing:13px;margin-top:6px">STRATEGIES</div></div>

  <div class="contact" style="left:210px">
    <div class="ring"><svg width="30" height="30" viewBox="0 0 24 24" fill="none" stroke="var(--gold)" stroke-width="1.8"><path d="M5 3h4l2 5-3 2a11 11 0 006 6l2-3 5 2v4a2 2 0 01-2 2A17 17 0 013 5a2 2 0 012-2z"/></svg></div>
    <div class="label">CALL ME 24/7</div>
    <div class="value">555-014-2873</div>
  </div>
  <div class="contact" style="left:468px">
    <div class="ring"><svg width="30" height="30" viewBox="0 0 24 24" fill="none" stroke="var(--gold)" stroke-width="1.8"><circle cx="12" cy="12" r="9"/><path d="M12 7v5l3 2"/></svg></div>
    <div class="label">RAPID CONTACT</div>
    <div class="value">WITHIN 12/HR</div>
  </div>
  <div class="contact" style="left:758px">
    <div class="ring"><svg width="30" height="30" viewBox="0 0 24 24" fill="none" stroke="var(--gold)" stroke-width="1.8"><rect x="3" y="6" width="18" height="12" rx="1"/><path d="M3 7l9 6 9-6"/></svg></div>
    <div class="label">MAIL US</div>
    <div class="value">info@halvern<br>strategies.example</div>
  </div>

  <div class="abs footer-rule"></div>
  <p class="abs copyright">Copyrights © 2021 Halvern Strategies. All Rights Reserved.</p>
  <span class="abs build">C20</span>
</footer>

</body>
</html>
```